Providing Back Office Solutions to Financial Advisors and Attorney Needs a Business Card Design

Need a Business Card Design that speaks to Financial Advisor and Attorneys. Some of the word that come to mind is Clean/Simple & Futuristic.

Industry/Entity Type

Business

```html
<!DOCTYPE html>
<html lang="en">
<head>
<meta charset="utf-8">
<title>Corvane Back Office Solutions — Business Card</title>
<link rel="stylesheet" href="https://fonts.googleapis.com/css2?family=Montserrat:wght@400;600;700&family=Roboto+Condensed:wght@700&family=Cabin:wght@600&display=swap">
<style>
  :root {
    --backdrop: #d9d6d2;
    --card: #eef1f2;
    --card-edge: #ffffff;
    --brand: #1e5c84;
    --tagline: #3d3b7c;
    --name: #1f4f78;
    --text: #3a3d40;
    --icon: #2b3b4a;
  }
  html, body {
    margin: 0;
    width: 1200px;
    height: 1054px;
    overflow: hidden;
    background: var(--backdrop);
  }
  .card {
    position: absolute;
    left: 80px;
    top: 214px;
    width: 1040px;
    height: 629px;
    background: var(--card);
    border: 2px solid var(--card-edge);
    box-sizing: border-box;
    font-family: "Montserrat", sans-serif;
    color: var(--text);
  }
  .brand-mark {
    position: absolute;
    left: 77px;
    top: 153px;
    width: 320px;
    height: 320px;
    border: 6px solid var(--brand);
    box-sizing: border-box;
  }
  .brand-name {
    position: absolute;
    right: 53px;
    top: 44px;
    margin: 0;
    font-family: "Montserrat", sans-serif;
    font-weight: 700;
    font-size: 80px;
    letter-spacing: 4px;
    line-height: 1;
    color: var(--brand);
  }
  .tagline {
    position: absolute;
    right: 53px;
    top: 174px;
    margin: 0;
    font-family: "Roboto Condensed", sans-serif;
    font-weight: 700;
    font-size: 38px;
    line-height: 1;
    color: var(--tagline);
  }
  .person {
    position: absolute;
    right: 53px;
    top: 314px;
    text-align: right;
  }
  .person-name {
    margin: 0;
    font-family: "Cabin", sans-serif;
    font-weight: 600;
    font-size: 37px;
    line-height: 1.1;
    color: var(--name);
  }
  .person-title {
    margin: 10px 0 0;
    font-size: 23px;
    line-height: 1.2;
  }
  .contacts {
    position: absolute;
    right: 53px;
    top: 436px;
    margin: 0;
    padding: 0;
    list-style: none;
    text-align: right;
    font-size: 23px;
  }
  .contact {
    display: flex;
    justify-content: flex-end;
    align-items: center;
    gap: 16px;
    height: 37px;
  }
  .contact svg {
    width: 22px;
    height: 22px;
    fill: var(--icon);
  }
  .contact.address {
    margin-top: 6px;
    font-size: 24px;
  }
</style>
</head>
<body>
  <section class="card" aria-label="Business card">
    <div class="brand-mark" aria-hidden="true"></div>

    <h1 class="brand-name">CORVANE</h1>
    <p class="tagline">BACK OFFICE SOLUTIONS</p>

    <div class="person">
      <p class="person-name">John Doe Smith</p>
      <p class="person-title">Managing Director</p>
    </div>

    <ul class="contacts">
      <li class="contact">
        <span>555.555.5555</span>
        <svg viewBox="0 0 24 24" aria-hidden="true"><path d="M4 9c0-3 4-5 8-5s8 2 8 5v2h-4V9c-1-.8-2.5-1-4-1s-3 .2-4 1v2H4z M7 12h10l3 7H4z"/></svg>
      </li>
      <li class="contact">
        <span>johndoe@example.com</span>
        <svg viewBox="0 0 24 24" aria-hidden="true"><path d="M2 5h20v14H2z M3.5 6.5 12 13l8.5-6.5v11h-17z" fill-rule="evenodd"/><path d="M3 6l9 7 9-7" fill="none" stroke="#eef1f2" stroke-width="1.5"/></svg>
      </li>
      <li class="contact">
        <span>www.yourwebsite.com</span>
        <svg viewBox="0 0 24 24" aria-hidden="true"><circle cx="12" cy="12" r="10"/><g fill="none" stroke="#eef1f2" stroke-width="1.3"><ellipse cx="12" cy="12" rx="4" ry="10"/><path d="M2 12h20M4 7h16M4 17h16M12 2v20"/></g></svg>
      </li>
      <li class="contact address">
        <span>234 Anywhere St., Any Town, US 123456</span>
      </li>
    </ul>
  </section>
</body>
</html>
```